SEAFOOD PACKAGING (Products for consumer)

We are looking to create packaging for various Tidewell such as octopus and squid. We plan to sell our products in upscale supermarkets.

We are specializing in cut octopus this time.

Please include our company logo. Also, please leave a transparent area so that customers can see the product inside.
Updates

We want to show what is inside, so a picture of the octopus is not required. We need something simple and sophisticated.

Target Market(s)

upscale store in US and ASIA

Industry/Entity Type

Fisheries dealer

Requirements
Must have
• Please include the attached logo,Blue one is preferred.Please leave a transparent part so that the contents of the product can be seen by the consumer.1. product name on packaging →CUT OCTOPUS,TAKO SASHIMI,Highest quality,Top quality etc... 3. What text information should be on the packaging →(It may be edited, but this is the image) The raw materials are caught in a very clean environment and processed in a modern factory with KVT certification. We are committed to additive-free products. 4. Packing size(cm/inch)→it will be about 19cm*22cm. 5. what kind of packaging do you use →PP or PA 6. dll →ai,jag
Nice to have
• https://plenvik.com/shots/4829173-Merulo-Prawn We need something simple and sophisticated like this one.
Should not have
• We want to show what is inside, so a picture of the octopus is not required. We need something simple and sophisticated.

```html
<!DOCTYPE html>
<html lang="en">
<head>
<meta charset="utf-8">
<title>Cut Octopus – Tako Sashimi Packaging</title>
<link rel="stylesheet" href="https://fonts.googleapis.com/css2?family=Open+Sans:ital,wght@1,400;1,800&family=Roboto+Condensed:wght@400;700&display=swap">
<style>
  :root {
    --page: #eef1f5;
    --bag: #ffffff;
    --ocean: #0a5fb4;
    --ocean-deep: #084e96;
    --ocean-light: #7fb0df;
    --ribbon-dark: #4f0d12;
    --ribbon-red: #e01b24;
    --badge-red: #d91e26;
    --white: #ffffff;
  }
  html, body {
    margin: 0;
    width: 1200px;
    height: 772px;
    overflow: hidden;
    background: var(--page);
  }
  .canvas {
    position: relative;
    width: 1200px;
    height: 772px;
  }
  .pack-front {
    position: absolute;
    left: 285px;
    top: 20px;
    width: 630px;
    height: 731px;
    background: var(--bag);
    box-shadow: 0 4px 18px rgba(10, 40, 80, 0.12);
  }
  .pack-front svg { display: block; width: 100%; height: 100%; }
  .brand-name { font-family: "Roboto Condensed", sans-serif; font-weight: 700; fill: var(--ocean); }
  .title-main { font-family: "Open Sans", sans-serif; font-style: italic; font-weight: 800; fill: var(--white); }
  .title-sub { font-family: "Open Sans", sans-serif; font-style: italic; font-weight: 400; fill: var(--white); }
  .claim { font-family: "Roboto Condensed", sans-serif; font-weight: 400; fill: var(--white); letter-spacing: 4px; }
  .story { font-family: "Roboto Condensed", sans-serif; font-weight: 400; fill: var(--white); }
  .net-weight { font-family: "Roboto Condensed", sans-serif; font-weight: 700; fill: var(--white); }
  .storage { font-family: "Roboto Condensed", sans-serif; font-weight: 400; fill: var(--white); }
  .badge-text { font-family: "Roboto Condensed", sans-serif; font-weight: 700; fill: var(--white); letter-spacing: 1px; }
</style>
</head>
<body>
<main class="canvas">
  <section class="pack-front">
    <svg viewBox="0 0 1085 1260" xmlns="http://www.w3.org/2000/svg">
      <defs>
        <linearGradient id="ribbon-fill" x1="0" x2="1" y1="0" y2="0">
          <stop offset="0" stop-color="var(--ribbon-dark)"/>
          <stop offset="0.45" stop-color="var(--ribbon-red)"/>
          <stop offset="1" stop-color="var(--ribbon-dark)"/>
        </linearGradient>
        <linearGradient id="sea-fill" x1="0" x2="0" y1="0" y2="1">
          <stop offset="0" stop-color="var(--ocean-light)"/>
          <stop offset="1" stop-color="var(--ocean)"/>
        </linearGradient>
        <path id="badge-ring" d="M805,635 m-54,0 a54,54 0 1,1 108,0 a54,54 0 1,1 -108,0"/>
      </defs>

      <!-- centre band -->
      <g class="centre-band">
        <rect x="382" y="0" width="325" height="1260" fill="var(--ocean)"/>
        <line x1="405" y1="0" x2="405" y2="900" stroke="var(--white)" stroke-width="2"/>
        <line x1="685" y1="0" x2="685" y2="900" stroke="var(--white)" stroke-width="2"/>
      </g>

      <!-- sea artwork at the foot -->
      <rect class="sea-artwork" x="0" y="840" width="1085" height="420" fill="url(#sea-fill)" role="img" aria-label="Blue engraved octopus tentacles and swirling wave pattern"/>

      <!-- information shield -->
      <g class="info-shield">
        <polygon points="272,895 795,895 795,1110 700,1190 700,1260 385,1260 385,1190 272,1110" fill="var(--ocean)"/>
        <polyline points="290,910 290,1102 400,1182 400,1260" fill="none" stroke="var(--white)" stroke-width="2"/>
        <polyline points="777,910 777,1102 685,1182 685,1260" fill="none" stroke="var(--white)" stroke-width="2"/>
      </g>

      <!-- clear product window -->
      <path class="product-window" role="img" aria-label="Octopus-shaped clear window showing the cut octopus inside"
        d="M200,780 C160,700 250,640 330,660 C330,590 420,560 480,600 C540,540 640,540 680,600 C720,540 810,540 830,620 C900,640 920,720 870,780 C920,830 880,900 820,880 C790,960 700,980 640,930 C600,990 470,990 430,930 C360,980 260,950 270,880 C180,880 150,820 200,780 Z"
        fill="var(--white)" stroke="var(--ocean)" stroke-width="10"/>

      <!-- brand marks -->
      <g class="maker-mark">
        <circle cx="185" cy="160" r="78" fill="none" stroke="var(--ocean)" stroke-width="6"/>
        <text class="brand-name" x="185" y="173" font-size="36" text-anchor="middle">TIDEWELL</text>
      </g>
      <g class="label-mark">
        <circle cx="920" cy="165" r="70" fill="none" stroke="var(--ocean)" stroke-width="6"/>
        <text class="brand-name" x="920" y="178" font-size="36" text-anchor="middle">MARLO</text>
      </g>

      <!-- product name ribbon -->
      <g class="name-ribbon">
        <path d="M270,285 C450,250 550,230 797,200 L797,380 C600,390 450,430 270,458 Z" fill="url(#ribbon-fill)"/>
        <text class="title-main" x="530" y="325" font-size="82" text-anchor="middle" transform="rotate(-9 530 325)">CUT OCTOPUS</text>
        <text class="title-sub" x="545" y="395" font-size="66" text-anchor="middle" transform="rotate(-9 545 395)">TAKO SASHIMI</text>
      </g>

      <!-- claim -->
      <g class="natural-claim">
        <rect x="437" y="490" width="208" height="40" rx="4" fill="none" stroke="var(--white)" stroke-width="2"/>
        <text class="claim" x="541" y="520" font-size="28" text-anchor="middle">ALL NATURAL</text>
      </g>

      <!-- no additives badge -->
      <g class="additive-badge">
        <circle cx="805" cy="635" r="76" fill="var(--badge-red)"/>
        <circle cx="805" cy="635" r="69" fill="none" stroke="var(--white)" stroke-width="3"/>
        <circle cx="805" cy="635" r="30" fill="var(--white)"/>
        <path d="M805,612 C796,626 790,636 790,645 A15,15 0 0,0 820,645 C820,636 814,626 805,612 Z" fill="var(--badge-red)"/>
        <text class="badge-text" font-size="20"><textPath href="#badge-ring">NO ADDITIVES • NO ADDITIVES •</textPath></text>
      </g>

      <!-- product story -->
      <g class="product-story">
        <text class="story" x="541" y="1025" font-size="26" text-anchor="middle">The raw materials are caught in a very clean environment</text>
        <text class="story" x="541" y="1060" font-size="26" text-anchor="middle">processed in a modern factory with KVT certification</text>
        <text class="net-weight" x="541" y="1150" font-size="36" text-anchor="middle">NET WT. 32 OZ (2.0 LB) 907g</text>
        <text class="storage" x="541" y="1195" font-size="26" text-anchor="middle">KEEP FROZEN</text>
      </g>
    </svg>
  </section>
</main>
</body>
</html>
```